Business Card for Business consulting practice

Need a design for a consultant business card. Simple and elegant.
I need the following information on the card:
Logo: (see uploaded file)
Company name: Calmora Advisory Group
Name: Dana Weltrup
Title: Managing Director - Aerospace and Defence
Phone #: 514-268-3917
e-mail: dana.weltrup@calmora-example.com
Website: www.calmora-example.com
Tagline: Proposals Management and Capture support for complex procurements

```html
<!DOCTYPE html>
<html lang="en">
<head>
<meta charset="utf-8">
<title>Calmora Advisory Group – Business Card</title>
<link href="https://fonts.googleapis.com/css2?family=Cinzel:wght@400;600&family=Montserrat:wght@400;500&display=swap" rel="stylesheet">
<style>
  :root {
    --navy: #0b2038;
    --navy-deep: #071628;
    --blue: #1b8fbd;
    --white: #ffffff;
    --silver: #c9ccd1;
    --bg: #e4e5e7;
  }
  * { box-sizing: border-box; margin: 0; padding: 0; }
  html, body { width: 1200px; height: 800px; overflow: hidden; background: var(--bg); }
  .canvas { position: relative; width: 1200px; height: 800px; }

  .card {
    position: absolute; top: 245px; width: 540px; height: 310px;
    border-radius: 22px; overflow: hidden;
  }
  .card-front { left: 40px; background: var(--white); }
  .card-back {
    left: 620px;
    background: radial-gradient(ellipse at 40% 40%, #13304f 0%, var(--navy) 55%, var(--navy-deep) 100%);
    display: flex; align-items: center; justify-content: center;
  }

  .emblem-area { position: absolute; right: 0; top: 0; width: 300px; height: 310px; }

  .front-info { position: absolute; left: 34px; top: 34px; width: 270px; }
  .company-name {
    font-family: "Cinzel", serif; font-weight: 600; color: var(--navy);
    font-size: 21px; line-height: 1.15; letter-spacing: 1px;
  }
  .company-rule { height: 1.5px; background: var(--blue); width: 230px; margin: 10px 0 12px; }
  .person-name {
    font-family: "Cinzel", serif; font-weight: 400; color: var(--navy);
    font-size: 20px; letter-spacing: 1px;
  }
  .person-title {
    font-family: "Montserrat", sans-serif; color: var(--blue);
    font-size: 11.5px; line-height: 1.35; margin-top: 3px;
  }
  .contact-list { list-style: none; margin-top: 14px; }
  .contact-list li {
    display: flex; align-items: center; gap: 8px;
    font-family: "Montserrat", sans-serif; color: var(--navy);
    font-size: 11px; line-height: 1.6;
  }
  .contact-list svg { width: 10px; height: 10px; fill: var(--blue); flex: none; }
  .tagline {
    font-family: "Montserrat", sans-serif; font-weight: 500; color: var(--blue);
    font-size: 11.5px; line-height: 1.35; margin-top: 14px;
  }

  .back-name {
    font-family: "Cinzel", serif; font-weight: 600; color: var(--silver);
    font-size: 34px; letter-spacing: 3px; text-align: center; line-height: 1.2;
  }
</style>
</head>
<body>
<main class="canvas">

  <section class="card card-front">
    <svg class="emblem-area" viewBox="0 0 300 310" role="img" aria-label="Large brand emblem area">
      <path d="M60 0 H300 V310 H230 Z" fill="#0b2038"/>
    </svg>

    <div class="front-info">
      <p class="company-name">CALMORA<br>ADVISORY GROUP</p>
      <div class="company-rule"></div>
      <p class="person-name">DANA WELTRUP</p>
      <p class="person-title">Managing Director<br>Aerospace &amp; Defence</p>
      <ul class="contact-list">
        <li>
          <svg viewBox="0 0 10 10"><path d="M2 0.5 L3.6 2.6 L2.7 3.6 Q3.8 5.9 6.4 7.3 L7.4 6.4 L9.5 8 L8.3 9.5 Q3.5 9 0.5 1.7 Z"/></svg>
          514-268-3917
        </li>
        <li>
          <svg viewBox="0 0 10 10"><path d="M0.5 2 H9.5 V8 H0.5 Z M0.5 2 L5 5.3 L9.5 2" fill="#1b8fbd" stroke="#fff" stroke-width="0.8"/></svg>
          dana.weltrup@calmora-example.com
        </li>
        <li>
          <svg viewBox="0 0 10 10"><circle cx="5" cy="5" r="4.5"/><path d="M0.5 5 H9.5 M5 0.5 Q2.5 5 5 9.5 M5 0.5 Q7.5 5 5 9.5" stroke="#fff" stroke-width="0.7" fill="none"/></svg>
          www.calmora-example.com
        </li>
      </ul>
      <p class="tagline">Proposals Management &amp;<br>Capture support for<br>complex procurements</p>
    </div>
  </section>

  <section class="card card-back">
    <p class="back-name">CALMORA<br>ADVISORY GROUP</p>
  </section>

</main>
</body>
</html>
```